General contractor/GM consaltant business card

I need a card for my contracting company in North Dakota, we build industrial buildings for the oil feild and oil feild related companies offices, shops, airplain hangars, airports ext. We have a familly atmosphere on the job and are very relational and personal.
Industry/Entity Type
Industrial
Contact Information for Business Card
Kestrelmoor Builders LLC.
Dwight T.Halvorsun
4736 Quillfern dr. Colorado Springs, CO. 80927
Cell# 406-555-8142
dwight@kestrelmoorbuilders.com

```html
<!DOCTYPE html>
<html lang="en">
<head>
<meta charset="utf-8">
<title>Kestrelmoor Builders LLC. – Business Card</title>
<link href="https://fonts.googleapis.com/css2?family=Arimo:wght@400;700&display=swap" rel="stylesheet">
<style>
  :root {
    --backdrop: #2b2b2b;
    --card-grey: #c4c5c8;
    --card-light: #eeeeef;
    --card-mid: #b9babd;
    --accent-red: #ee1c25;
    --ink: #1a1a1a;
  }
  * { box-sizing: border-box; margin: 0; padding: 0; }
  html, body {
    width: 1200px;
    height: 799px;
    overflow: hidden;
    background: var(--backdrop);
    font-family: "Arimo", Arial, sans-serif;
  }
  .sheet {
    position: relative;
    width: 1200px;
    height: 799px;
    display: flex;
    align-items: center;
    justify-content: center;
    gap: 50px;
  }
  .card {
    position: relative;
    width: 520px;
    height: 300px;
    overflow: hidden;
    box-shadow: 0 12px 30px rgba(0,0,0,0.5);
  }
  .card-front { background: var(--card-grey); }
  .card-back {
    background: radial-gradient(ellipse at 55% 40%, var(--card-light) 0%, var(--card-mid) 75%);
  }
  .edge-bar {
    position: absolute;
    width: 10px;
    background: var(--accent-red);
  }
  .card-front .edge-bar.left { left: 0; top: 40px; height: 150px; }
  .card-front .edge-bar.right { right: 0; top: 140px; height: 150px; }
  .card-back .edge-bar.left { left: 0; top: 70px; height: 160px; }
  .card-back .edge-bar.right { right: 0; top: 160px; height: 130px; }

  .brand {
    position: absolute;
    left: 0; right: 0; top: 0; bottom: 0;
    display: flex;
    align-items: center;
    justify-content: center;
    gap: 12px;
  }
  .brand-dot {
    width: 18px; height: 18px;
    border-radius: 50%;
    background: var(--accent-red);
  }
  .brand-name {
    color: var(--accent-red);
    font-weight: 700;
    font-size: 26px;
  }

  .contact {
    position: absolute;
    left: 60px;
    top: 115px;
    display: flex;
    align-items: flex-start;
  }
  .holder-name {
    color: var(--ink);
    font-size: 18px;
    padding-top: 10px;
    padding-right: 14px;
  }
  .divider {
    width: 1.5px;
    height: 58px;
    background: var(--accent-red);
    margin-right: 14px;
  }
  .details { font-size: 15px; line-height: 1.2; }
  .address { color: var(--accent-red); margin-bottom: 2px; }
  .line { color: var(--ink); display: flex; align-items: center; gap: 4px; }
  .line svg { width: 11px; height: 11px; flex: none; }
</style>
</head>
<body>
<main class="sheet">
  <section class="card card-front">
    <span class="edge-bar left"></span>
    <span class="edge-bar right"></span>
    <div class="brand">
      <span class="brand-dot"></span>
      <span class="brand-name">Kestrelmoor Builders LLC.</span>
    </div>
  </section>

  <section class="card card-back">
    <span class="edge-bar left"></span>
    <span class="edge-bar right"></span>
    <div class="contact">
      <p class="holder-name">Dwight T.Halvorsun</p>
      <span class="divider"></span>
      <div class="details">
        <p class="address">4736 Quillfern<br>dr. Colorado Springs<br>CO. 80927</p>
        <p class="line">
          <svg viewBox="0 0 12 12" aria-hidden="true"><circle cx="6" cy="6" r="5" fill="none" stroke="#1a1a1a" stroke-width="1"/><rect x="3.3" y="4" width="5.4" height="4" fill="none" stroke="#1a1a1a" stroke-width="0.8"/><path d="M3.3 4 L6 6.2 L8.7 4" fill="none" stroke="#1a1a1a" stroke-width="0.8"/></svg>
          dwight@kestrelmoorbuilders.com
        </p>
        <p class="line">
          <svg viewBox="0 0 12 12" aria-hidden="true"><circle cx="6" cy="6" r="5" fill="none" stroke="#1a1a1a" stroke-width="1"/><path d="M4.2 3.5 C4 5.5 5.8 8 8 8 L8.3 7 L7.2 6.5 L6.7 7 C6 6.6 5.3 5.9 5 5.2 L5.5 4.7 L5 3.6 Z" fill="#1a1a1a"/></svg>
          406-555-8142
        </p>
      </div>
    </div>
  </section>
</main>
</body>
</html>
```